Math Help Website Needs New Design

Looking to refresh the design of my existing site (brightsumguide.net) to be easier on the eyes. I am fully capable of doing the HTML coding and have for years, but I don't have the eye for good design, colors, layout, and fonts. This is where I need help!

I need both a new design scheme and a new logo that matches. The overall functionality will be the same as the existing site, and should not be unrecognizable.

Target Market(s)

It should appeal to students (age 13-22) and their parents, so it should NOT be childish in appearance, nor should it be corporate.

Requirements
Must have
• Should be simple, easy-to-navigate, and neither childish nor corporate. I am looking for a design for both the homepage and a similar "content" page. Simple, bold colors are preferred. A logo should be prominent at the top, with a search bar nearby. Below that I need a similar navigational area like I already have. Then, I need about 200px wide ad space on the left of the main body area.

```html
<!DOCTYPE html>
<html lang="en">
<head>
<meta charset="utf-8">
<title>BrightSum Guide</title>
<link href="https://fonts.googleapis.com/css2?family=Montserrat:wght@400;600;700&family=Open+Sans:wght@400;600;700&display=swap" rel="stylesheet">
<style>
:root{
  --green:#6cb33f; --green-dark:#4f9a2a; --green-light:#c9e3a6;
  --cyan:#1fc1ea; --cyan-dark:#0aa9d3;
  --orange:#f08a12; --red:#d4440f; --red-dark:#b8360a;
  --text:#333; --muted:#777; --line:#ddd; --input:#ffe2a0; --pink:#d9697a;
}
*{box-sizing:border-box;margin:0;padding:0}
html,body{width:768px;height:1200px;overflow:hidden}
body{position:relative;font-family:"Open Sans",sans-serif;color:var(--text);
  background:linear-gradient(#fff 0,#fff 143px,#a7d37c 143px,var(--green) 600px,var(--green-dark) 1200px)}
.abs{position:absolute}
.brand{left:77px;top:20px;font:700 20px "Montserrat",sans-serif;color:var(--green);display:flex;align-items:center;gap:7px;white-space:nowrap}
.brand .dot{width:12px;height:12px;border-radius:50%;background:var(--cyan)}
.online{left:347px;top:22px;width:197px;height:19px;border-radius:10px;background:var(--green);color:#fff;font-size:7.6px;line-height:19px;padding-left:11px;white-space:nowrap;overflow:hidden}
.online b{font-weight:700}
.search{left:553px;top:22px;width:136px;height:19px;border-radius:10px;border:1px solid #ccc;background:#f3f3f3;font-size:8.5px;color:#999;line-height:17px;padding-left:12px}
.nav{left:77px;top:60px;width:614px;height:32px;background:var(--cyan);border-radius:4px 4px 0 0;display:flex;align-items:center;justify-content:space-between;padding:0 12px 0 6px}
.nav a{font:600 10px "Montserrat",sans-serif;color:#fff;text-decoration:none;padding:3px 8px;white-space:nowrap}
.nav a.active{background:#e9f8fc;color:var(--cyan-dark);border-radius:11px;padding:3px 13px}
.page{left:77px;top:91px;width:614px;height:1017px;background:#fff;border-radius:0 0 4px 4px}
.hero{left:88px;top:104px;width:590px;height:212px;border:1px solid #d4e6ee;background:linear-gradient(90deg,#f4fbfd 0,#e3f4fa 45%,#bfe6f2 100%);overflow:hidden}
.hero h1{position:absolute;left:27px;top:22px;font:600 29px/1.1 "Montserrat",sans-serif;color:#222;white-space:nowrap;z-index:1}
.hero h1 span{color:var(--red)}
.hero p{position:absolute;left:27px;top:92px;width:250px;font-size:9px;line-height:14px;color:#333;z-index:1}
.hero p span{color:#e01010}
.cta{position:absolute;left:27px;top:161px;height:27px;width:168px;background:var(--red);color:#fff;font:700 12px/27px "Montserrat",sans-serif;padding-left:28px;white-space:nowrap;clip-path:polygon(0 0,92% 0,100% 50%,92% 100%,0 100%)}
.cta svg{position:absolute;left:9px;top:8px}
.hero-art{position:absolute;left:300px;top:0;width:289px;height:210px;background:linear-gradient(135deg,rgba(160,220,225,.0),#9fd8e6 55%,#7ec8dc)}
.adbox{left:88px;top:340px;width:153px;height:155px;border:1px solid #ddd;background:#fff}
.adbox .ad{position:absolute;left:16px;top:16px;width:121px;height:121px;border:1px solid #a4c34a;display:flex;flex-direction:column;align-items:center;justify-content:center;gap:8px}
.adbox .sq{width:34px;height:34px;background:#3aa3c9}
.adbox .ad span{font:700 11px/1.2 "Montserrat",sans-serif;color:#2a8fbf;text-align:center}
.tile{top:340px;width:209px;height:143px;color:#fff;padding:14px 16px}
.tile h2{font:600 15px "Montserrat",sans-serif;margin-bottom:6px}
.tile li{list-style:none;font-size:10px;line-height:14.5px;padding-left:14px;position:relative;white-space:nowrap}
.tile li:before{content:"";position:absolute;left:1px;top:4px;width:7px;height:4px;border-left:2px solid #fff;border-bottom:2px solid #fff;transform:rotate(-45deg)}
.tile .more{position:absolute;left:16px;bottom:9px;width:108px;height:13px;border-radius:7px;background:#eee;font:600 7px/13px "Montserrat",sans-serif;text-align:center}
.new{left:252px;background:linear-gradient(135deg,#66b82b,#3e9a22)}
.new .more{color:var(--green-dark)}
.lessons{left:470px;background:linear-gradient(135deg,#f6a11a,#ec7a0b)}
.lessons .more{color:var(--red)}
.lessons .art{position:absolute;right:14px;top:38px;width:72px;height:72px;background:rgba(200,60,10,.35);border-radius:6px}
.study{left:88px;top:496px;width:153px;height:314px;background:var(--cyan);overflow:hidden}
.study h3{height:42px;display:flex;align-items:center;gap:7px;padding-left:10px;font:600 12px "Montserrat",sans-serif;color:#fff}
.study h3 i{width:20px;height:20px;border-radius:50%;background:#fff;display:inline-block}
.post{display:flex;gap:8px;padding:8px 8px 0 10px;border-top:1px solid rgba(255,255,255,.35);color:#fff;font-size:7.8px;line-height:10.4px}
.post i{flex:none;width:22px;height:22px;background:#eef2f3;border-radius:3px}
.post i.pic{background:#556066}
.ask{left:88px;top:810px;width:153px;height:120px;background:linear-gradient(#e3e3e3,#cfcfcf);padding:12px 10px}
.ask h3{font:600 12px "Montserrat",sans-serif;color:#444;margin-bottom:3px}
.ask p{font-size:7.8px;line-height:10.4px;color:#555;width:86px}
.ask .art{position:absolute;right:6px;top:42px;width:52px;height:76px;background:linear-gradient(#e8c9a6,#7fcf5c);border-radius:24px 24px 4px 4px}
.disc-title{left:252px;top:508px;font:600 16px "Montserrat",sans-serif;color:var(--cyan-dark)}
.pill{left:569px;top:510px;width:108px;height:13px;border-radius:7px;background:#dedede;color:var(--cyan-dark);font:600 7px/13px "Montserrat",sans-serif;text-align:center}
.disc{left:252px;top:532px;width:425px;height:161px;border:1px solid #ddd}
.disc .photo{position:absolute;left:7px;top:7px;width:145px;height:146px;background:linear-gradient(135deg,#3d4a50,#6c7a82 60%,#7a3f9a)}
.thread{position:absolute;left:160px;width:250px;font-size:8.3px;line-height:11px;padding-bottom:5px;border-bottom:1px solid #eee;white-space:nowrap}
.thread a{color:var(--cyan-dark);text-decoration:none;font-size:8.5px}
.thread small{display:block;color:var(--green-dark);font-size:7.5px}
.tabs{left:252px;top:710px;width:421px;height:22px;border-bottom:2px solid var(--red);display:flex;align-items:flex-end;justify-content:space-between;font-size:9px;white-space:nowrap}
.tabs span{padding:4px 5px}
.tabs .on{background:var(--red);color:#fff;padding:4px 7px}
.tabs .gap{margin-left:14px}
.sym{left:254px;top:746px}
.label{left:257px;font:700 8.5px "Open Sans",sans-serif;color:#333}
.field{left:347px;width:325px}
.problem{top:817px;height:39px;background:var(--input);font-size:8.5px;color:#8a7a55;padding:11px 12px}
.examples{top:862px;height:115px;border:1px solid #ccc;background:#f2f2f2;padding:12px 18px;font-size:8.3px;line-height:17px;color:#888}
.btn{left:346px;height:21px;width:80px;background:var(--red);color:#fff;font:700 8.5px/21px "Open Sans",sans-serif;padding-left:10px;white-space:nowrap;clip-path:polygon(0 0,88% 0,100% 50%,88% 100%,0 100%)}
.select{top:1016px;height:26px;border:1px solid #ccc;background:#f2f2f2}
.select:after{content:"";position:absolute;right:8px;top:6px;width:8px;height:12px;border-left:1px solid #ccc}
.footer{left:0;width:768px;text-align:center;color:#fff;font-size:8.5px}
.footer a{color:#fff;text-decoration:none}
</style>
</head>
<body>
<div class="abs brand"><span class="dot"></span>BrightSum Guide</div>
<div class="abs online"><b>57 People Online</b> They can help you right now</div>
<div class="abs search">Search</div>

<div class="abs page"></div>
<nav class="abs nav">
  <a href="#">HOME</a><a class="active" href="#">ALGEBRA</a><a href="#">GEOMETRY</a><a href="#">TRIG</a><a href="#">CALCULUS</a><a href="#">STATISTICS</a><a href="#">MORE SUBJECTS</a><a href="#">MESSAGE BOARD</a>
</nav>

<section class="abs hero">
  <div class="hero-art" role="img" aria-label="Large pale blue numerals with a cheerful boy in a blue shirt"></div>
  <h1>Welcome to<br><span>BRIGHTSUM</span> Guide</h1>
  <p><span>Math Lessons</span> - Looking to understand a subject better, or maybe you don't understand what your textbook is trying to tell you? We have a collection of algebra and geometry lessons that you can view online right now.</p>
  <div class="cta"><svg width="12" height="10" viewBox="0 0 12 10"><path d="M1 5l3.5 3.5L11 1" stroke="#fff" stroke-width="2.2" fill="none"/></svg>GET STARTED NOW</div>
</section>

<aside class="abs adbox"><div class="ad"><span class="sq"></span><span>Core Study<br>Circle</span></div></aside>

<section class="abs tile new">
  <h2>What's New?</h2>
  <ul><li>Multiplying Polynomials</li><li>Derivative of an Inverse Function</li><li>Derivatives of Logs and Exps</li><li>Differentiating Trig Functions</li></ul>
  <div class="more">MORE MATH LESSONS</div>
</section>
<section class="abs tile lessons">
  <h2>Math Lessons</h2>
  <ul><li>Algebra</li><li>Geometry</li><li>Trigonometry</li><li>Calculus</li><li>Statistics</li></ul>
  <div class="art" role="img" aria-label="Sketch of a compass, set square and math symbols"></div>
  <div class="more">MORE MATH LESSONS</div>
</section>

<section class="abs study">
  <h3><i></i>Live Study Group</h3>
  <div class="post" style="height:80px"><i></i><p>At the half-time show, a marching band marched in formation. The lead drummer started at a point with coordinates (-2, -5) and moved 3 steps...</p></div>
  <div class="post" style="height:70px"><i class="pic"></i><p>Write the direct variation equation for the following: y varies directly with x and y = 60 when x = 10</p></div>
  <div class="post" style="height:56px"><i></i><p>how do I do this question? see attached</p></div>
  <div class="post" style="height:66px"><i></i><p>Compute the discriminant of the quadratic equation</p></div>
</section>
<section class="abs ask">
  <h3>Ask Your Question</h3>
  <p>On our math help message board. Just be sure to explain what you've tried to do and where you're stuck, and a friendly volunteer may try to assist you!</p>
  <div class="art" role="img" aria-label="Smiling girl in a green top"></div>
</section>

<h2 class="abs disc-title">Current Discussions</h2>
<div class="abs pill">MORE MATH LESSONS</div>
<section class="abs disc">
  <div class="photo" role="img" aria-label="Teacher in a purple top standing at a chalkboard of equations"></div>
  <div class="thread" style="top:14px"><a href="#">Help!! Metric Units</a><br>I don't getany of this. all I know is that a kilometer is 1000...<small>Posted by: SamK</small></div>
  <div class="thread" style="top:58px"><a href="#">Calculating percentile and standard d...</a><br>I don't getany of this. all I know is that a kilometer is 1000...<small>Posted by: ProfLee</small></div>
  <div class="thread" style="top:102px;border:0"><a href="#">Linear word problem</a><br>I need help solving this: In order to obtain maximum...<small>Posted by: SamK</small></div>
</section>

<div class="abs tabs"><span>Basic Math</span><span class="on">Pre-Algebra</span><span>Algebra</span><span>Trigonometry</span><span class="gap">Precalculus</span><span>Calculus</span><span>Statistics</span></div>

<svg class="abs sym" width="420" height="55" viewBox="0 0 420 55" font-family="Open Sans,sans-serif" font-size="8" fill="none" stroke="#d9697a" stroke-width="1.2">
  <g fill="#eee" stroke="#ccc" stroke-width=".8">
    <rect x="2" y="2" width="18" height="18"/><rect x="36" y="2" width="18" height="18"/><rect x="70" y="2" width="18" height="18"/><rect x="104" y="2" width="18" height="18"/><rect x="138" y="2" width="18" height="18"/><rect x="172" y="2" width="18" height="18"/><rect x="206" y="2" width="18" height="18"/><rect x="240" y="2" width="18" height="18"/><rect x="274" y="2" width="18" height="18"/><rect x="308" y="2" width="18" height="18"/><rect x="342" y="2" width="18" height="18"/><rect x="376" y="2" width="18" height="18"/>
  </g>
  <g fill="#d9697a" stroke="none" text-anchor="middle">
    <text x="11" y="14">(▭)</text><text x="45" y="14">|▭|</text><text x="79" y="14">|▭|</text><text x="113" y="14">▭</text><text x="147" y="14">▭²</text><text x="181" y="14">√▭</text><text x="215" y="14">∜▭</text><text x="249" y="14">(▭)</text><text x="283" y="14">[▭]</text><text x="317" y="14">(▭)</text><text x="351" y="15" font-size="12">≥</text><text x="385" y="15" font-size="12">≤</text>
  </g>
  <rect x="4" y="35" width="14" height="14"/>
  <circle cx="45" cy="42" r="7.5"/>
  <path d="M79 35l8 14H71z"/>
  <path d="M108 35h14l-4 14h-14z"/>
  <path d="M142 36h10l4 13h-18z"/>
  <path d="M175 38h10v11h-10zM175 38l4-3h10l-4 3M189 35v11l-4 3"/>
  <ellipse cx="215" cy="37" rx="7" ry="2.5"/><path d="M208 37v11M222 37v11"/><ellipse cx="215" cy="48" rx="7" ry="2.5"/>
  <path d="M249 34l-7 14M249 34l7 14"/><ellipse cx="249" cy="48" rx="7" ry="2"/>
  <path d="M283 34l-8 15h16zM283 34l2 15"/>
  <circle cx="317" cy="42" r="7.5"/><ellipse cx="317" cy="42" rx="7.5" ry="2.5"/>
  <g fill="#d9697a" stroke="none" text-anchor="middle"><text x="351" y="47" font-size="12">÷</text><text x="385" y="47" font-size="11" font-style="italic">π</text></g>
</svg>

<div class="abs label" style="top:819px">Enter Problem:</div>
<div class="abs field problem">enter your problem here.....</div>
<div class="abs label" style="top:864px">Examples:</div>
<div class="abs field examples">Expand , Variables, Expressions, and Integers<br>Simplifying and Evaluating Expressions<br>Solving Equations<br>Multi-Step Equations and Inequalities<br>Factors, Fractions, and Exponents</div>
<div class="abs label" style="top:985px">Math Format</div>
<div class="abs btn" style="top:985px">Show Result</div>
<div class="abs label" style="top:1024px">Select Topic</div>
<div class="abs field select"></div>
<div class="abs btn" style="top:1051px">Find Answer</div>

<footer>
  <div class="abs footer" style="top:1129px"><a href="#">Home</a> | <a href="#">Algebra</a> | <a href="#">Geometry</a> | <a href="#">Trig</a> | <a href="#">Calculus</a> | <a href="#">Statistics</a> | <a href="#">More Subjects</a> | <a href="#">Message Board</a></div>
  <div class="abs footer" style="top:1143px">All Right Reserved Copyright © 2013 - Privacy Policy | Terms</div>
  <div class="abs footer" style="top:1157px;font-size:7.5px">Powered By Pixelmoor Studio</div>
</footer>
</body>
</html>
```